Floral Perfume Box Project for a high end boutique perfumery

I would like a design for a perfume box that has the following flowers on it: Gardenia, Lily of the valley, Freesia, jasmine, Rose. Metalic, gold highlights would be nice. The box should have a modern artistic look with both embossed and raised designs. Combine the Velmont Perfume (Lady Velmont) with the Harrow Ostrela box

Target Market(s)

Women ready to be married: This perfume is a wedding day scent

Industry/Entity Type

Boutique

Font styles to use
Sans Serif
Decorative

Colors

Designer to choose colors to be used in the design.

Requirements
Must have
• Similar design to Velmont , please see the velmont perfume images.
• The box must be white. The details should be done to the flowers with gold and silver high lights we will be using foil printing.
Nice to have
• gold highlights would be nice. The box should have a modern artistic look with both embossed and raised designs.
Should not have
• The box cannot be colored it must be white . The best art will be determined by the details of the flowers.

```html
<!DOCTYPE html>
<html lang="en">
<head>
<meta charset="UTF-8">
<title>Bridelle Bloom — Box Front</title>
<link rel="stylesheet" href="https://fonts.googleapis.com/css2?family=Allura&display=swap">
<style>
  :root {
    --page-bg: #efe9ec;
    --box-white: #f8f7f9;
    --box-shade: #e6e5ea;
    --petal-light: #f7e2df;
    --petal-mid: #efc9c4;
    --petal-deep: #e0aaa8;
    --petal-pale: #f4eef0;
    --dot: #c9586f;
    --berry: #a52a52;
    --gold-light: #f1d98a;
    --gold-mid: #c9a44a;
    --gold-dark: #9c7a2c;
  }
  * { margin: 0; padding: 0; box-sizing: border-box; }
  html, body {
    width: 1200px;
    height: 1128px;
    overflow: hidden;
    background: var(--page-bg);
  }
  .canvas {
    position: relative;
    width: 1200px;
    height: 1128px;
  }
  .box-front {
    position: absolute;
    left: 240px;
    top: 44px;
    width: 720px;
    height: 1040px;
    background: linear-gradient(160deg, var(--box-white) 0%, var(--box-shade) 100%);
    overflow: hidden;
    box-shadow: 0 2px 10px rgba(120, 90, 110, 0.15);
  }
  .artwork {
    position: absolute;
    inset: 0;
    width: 720px;
    height: 1040px;
  }
  .accent-dots circle { fill: var(--dot); }
  .title {
    position: absolute;
    inset: 0;
    font-family: "Allura", cursive;
    font-weight: 400;
    color: var(--berry);
  }
  .title__main {
    position: absolute;
    left: 92px;
    top: 400px;
    font-size: 168px;
    line-height: 1;
    white-space: nowrap;
  }
  .title__sub {
    position: absolute;
    right: 118px;
    top: 560px;
    font-size: 112px;
    line-height: 1;
    white-space: nowrap;
  }
</style>
</head>
<body>
  <main class="canvas">
    <section class="box-front">
      <svg class="artwork" viewBox="0 0 720 1040" aria-hidden="true">
        <defs>
          <radialGradient id="petalFill" cx="0.5" cy="0.5" r="0.6">
            <stop offset="0" stop-color="var(--petal-deep)"/>
            <stop offset="0.55" stop-color="var(--petal-mid)"/>
            <stop offset="1" stop-color="var(--petal-light)"/>
          </radialGradient>
          <radialGradient id="paleFill" cx="0.5" cy="0.5" r="0.6">
            <stop offset="0" stop-color="#ffffff"/>
            <stop offset="1" stop-color="var(--petal-pale)"/>
          </radialGradient>
          <linearGradient id="goldStroke" x1="0" y1="0" x2="1" y2="1">
            <stop offset="0" stop-color="var(--gold-light)"/>
            <stop offset="0.45" stop-color="var(--gold-mid)"/>
            <stop offset="0.7" stop-color="var(--gold-light)"/>
            <stop offset="1" stop-color="var(--gold-dark)"/>
          </linearGradient>
        </defs>

        <g class="floral-pale" role="img" aria-label="Faint white blossoms in the background at left and lower right">
          <ellipse cx="40" cy="180" rx="110" ry="120" fill="url(#paleFill)"/>
          <ellipse cx="600" cy="900" rx="130" ry="120" fill="url(#paleFill)"/>
        </g>

        <g class="floral floral--top" role="img" aria-label="Cluster of blush pink magnolia blossoms across the top">
          <ellipse cx="250" cy="120" rx="130" ry="110" fill="url(#petalFill)"/>
          <ellipse cx="380" cy="60" rx="90" ry="70" fill="url(#petalFill)"/>
          <ellipse cx="560" cy="160" rx="170" ry="170" fill="url(#petalFill)"/>
          <ellipse cx="680" cy="420" rx="70" ry="140" fill="url(#petalFill)"/>
        </g>

        <g class="floral floral--left" role="img" aria-label="Pink blossoms along the left edge">
          <ellipse cx="20" cy="540" rx="80" ry="140" fill="url(#petalFill)"/>
        </g>

        <g class="floral floral--bottom" role="img" aria-label="Cluster of blush pink magnolia blossoms across the bottom">
          <ellipse cx="90" cy="840" rx="150" ry="170" fill="url(#petalFill)"/>
          <ellipse cx="300" cy="760" rx="100" ry="70" fill="url(#petalFill)"/>
          <ellipse cx="370" cy="900" rx="150" ry="130" fill="url(#petalFill)"/>
          <ellipse cx="200" cy="990" rx="110" ry="60" fill="url(#petalFill)"/>
        </g>

        <g class="accent-dots">
          <circle cx="12" cy="160" r="5"/>
          <circle cx="92" cy="298" r="12"/>
          <circle cx="150" cy="240" r="6"/>
          <circle cx="38" cy="318" r="5"/>
          <circle cx="645" cy="620" r="12"/>
          <circle cx="570" cy="790" r="12"/>
          <circle cx="640" cy="812" r="10"/>
          <circle cx="650" cy="878" r="7"/>
          <circle cx="662" cy="928" r="5"/>
        </g>

        <circle cx="357" cy="519" r="335" fill="none" stroke="url(#goldStroke)" stroke-width="6"/>
      </svg>

      <h1 class="title">
        <span class="title__main">Bridelle</span>
        <span class="title__sub">Bloom</span>
      </h1>
    </section>
  </main>
</body>
</html>
```